DL SIZED ONE SIDED BROCHURE FOR CLEANING AND GARDENING SERVICE

business name: K&T property services
services provided: Strata cleaning,lawn mowing,hedge trimming,garden maintainance,lawn repair,weed spraying/removal, rubbish removal.
10 years experience and fully insured.
obligation free quotes.
phone number:contact doug 0427391054
email: ktpropertyservices@mailvane.example
slogan: when quality matters ring K&T
K&T logo would be nice but not essential
DL size in inches: 3.9in × 8.2in
DL size in millimetres: 100mm × 210mm
DL size in centimetres: 10cm x 21cm
Updates
doing good guys no suggestions except being original
Target Market(s)
real estate agents, private home owners, contractors.
Industry/Entity Type
Business
Look and feel
Each slider illustrates characteristics of the customer's brand and the style your logo design should communicate.

```html
<!DOCTYPE html>
<html lang="en">
<head>
<meta charset="utf-8">
<title>K&amp;T Property Services – DL Brochure</title>
<link href="https://fonts.googleapis.com/css2?family=Lato:wght@400;700&amp;family=Nothing+You+Could+Do&amp;display=swap" rel="stylesheet">
<style>
  :root {
    --panel-dark: #231f20;
    --brand-blue: #1ba9e1;
    --band-ink: #1c2329;
    --white: #ffffff;
    --block-black: #0b0b0b;
    --script-ink: #1d1a17;
  }
  * { margin: 0; padding: 0; box-sizing: border-box; }
  html, body {
    width: 1200px; height: 571px; overflow: hidden; background: #ffffff;
  }
  .brochure {
    position: relative; width: 1200px; height: 571px; overflow: hidden;
    font-family: "Lato", "Helvetica Neue", Arial, sans-serif;
  }

  /* Photo collage */
  .collage { position: absolute; left: 0; top: 0; width: 678px; height: 503px; }
  .photo { position: absolute; }
  .photo--hedge-worker {
    left: 0; top: 0; width: 345px; height: 250px;
    background: linear-gradient(160deg, #4f5a3a 0%, #8c8f7a 45%, #d9d6cf 70%, #6f6b5e 100%);
  }
  .photo--flowers {
    left: 345px; top: 0; width: 145px; height: 250px;
    background: linear-gradient(180deg, #6f8a35 0%, #c9c44a 35%, #d8d2c2 65%, #b9b3a5 100%);
  }
  .photo--mower {
    left: 490px; top: 0; width: 188px; height: 250px;
    background: linear-gradient(180deg, #4a7fc4 0%, #9fbfe0 35%, #3b3b3b 60%, #4f9a2c 80%, #2f7a1f 100%);
  }
  .photo--trimmer {
    left: 0; top: 250px; width: 345px; height: 253px;
    background: linear-gradient(170deg, #4d6a3a 0%, #7a6b3c 30%, #7aa04a 65%, #9cc06a 100%);
  }
  .photo--cleaning {
    left: 345px; top: 250px; width: 333px; height: 253px;
    background: linear-gradient(180deg, #ecebe8 0%, #dcdcd8 40%, #c48a4f 62%, #a9683a 100%);
  }

  /* Name block: plain square with the business name in the text font */
  .name-block {
    position: absolute; left: 197px; top: 103px; width: 293px; height: 294px;
    background: var(--block-black);
    display: flex; flex-direction: column; align-items: center; justify-content: center;
    color: var(--white); font-weight: 400; text-align: center;
  }
  .name-block__name { font-size: 76px; line-height: 1; letter-spacing: 1px; }
  .name-block__descriptor {
    margin-top: 28px; font-size: 31px; line-height: 1.12; letter-spacing: 0.5px;
  }

  .slogan {
    position: absolute; left: 150px; top: 412px;
    font-family: "Nothing You Could Do", cursive;
    font-size: 33px; line-height: 1; color: var(--script-ink); white-space: nowrap;
  }

  /* Service panel */
  .services {
    position: absolute; left: 678px; top: 0; width: 522px; height: 503px;
    background: var(--panel-dark); color: var(--white);
    padding: 64px 0 0 55px;
  }
  .services__title { font-size: 34px; font-weight: 400; line-height: 1; letter-spacing: 0.3px; }
  .services__list { list-style: none; margin-top: 18px; }
  .services__item {
    position: relative; padding-left: 37px;
    font-size: 22px; line-height: 34.4px; letter-spacing: 0.4px;
  }
  .services__item::before {
    content: ""; position: absolute; left: 4px; top: 13px;
    width: 9px; height: 9px; background: var(--white);
  }
  .contact { margin-top: 16px; }
  .contact__lead { font-size: 22px; letter-spacing: 0.3px; }
  .contact__phone {
    margin-top: 10px; font-size: 27px; font-weight: 700; color: var(--brand-blue);
    letter-spacing: 0.4px;
  }
  .contact__email { margin-top: 10px; font-size: 17px; letter-spacing: 0.3px; }

  /* Bottom band */
  .credentials-band {
    position: absolute; left: 0; top: 503px; width: 1200px; height: 68px;
    background: var(--brand-blue);
    display: flex; align-items: center; justify-content: center;
    font-size: 21px; font-weight: 700; letter-spacing: 4.5px; color: var(--band-ink);
  }
</style>
</head>
<body>
  <main class="brochure">
    <section class="collage">
      <div class="photo photo--hedge-worker" role="img" aria-label="Photo of a gardener in a cap trimming a tall hedge"></div>
      <div class="photo photo--flowers" role="img" aria-label="Photo of yellow flowering shrubs beside a house wall"></div>
      <div class="photo photo--mower" role="img" aria-label="Photo of a man pushing a red lawn mower across green grass"></div>
      <div class="photo photo--trimmer" role="img" aria-label="Photo of a gloved hand using a hedge trimmer on a green hedge"></div>
      <div class="photo photo--cleaning" role="img" aria-label="Photo of a mop, broom, bucket and cleaning bottles on a polished wooden floor"></div>

      <div class="name-block">
        <div class="name-block__name">K&amp;T</div>
        <div class="name-block__descriptor">PROPERTY<br>SERVICES</div>
      </div>

      <p class="slogan">When quality matters ring K&amp;T</p>
    </section>

    <section class="services">
      <h2 class="services__title">Our services include...</h2>
      <ul class="services__list">
        <li class="services__item">Strata cleaning</li>
        <li class="services__item">Lawn mowing</li>
        <li class="services__item">Hedge trimming</li>
        <li class="services__item">Garden maintainance</li>
        <li class="services__item">Lawn repair</li>
        <li class="services__item">Weed spraying/removal</li>
        <li class="services__item">Rubbish removal</li>
      </ul>
      <div class="contact">
        <p class="contact__lead">For obligation free quote contact:</p>
        <p class="contact__phone">Doug 0427 391 054</p>
        <p class="contact__email">ktpropertyservices@mailvane.example</p>
      </div>
    </section>

    <footer class="credentials-band">10 YEARS EXPERIENCE &amp; FULLY INSURED</footer>
  </main>
</body>
</html>
```